Gumleaf Plant Hire Business Card Design

Gumleaf Plant Hire Pty Ltd

WET or DRY HIRE

Kestrel M4-7 + attachments
Turf Cutter
Lawn mowers with catchers
Brushcutters
Blowers

We require a business card with the above information for a new equipment hire Company. Would like to see a redish/brown background or something to do with an Australian Red Dog (Cattle Dog) on the business card as our Logo - even some sort of watermark as a background.

ABN: 81 327 905 168
17C Korrin Street Carrowvale Qld 4731
PO Box 8150 Carrowvale Qld 4731
PH: 0417302968 or 0438715024
Email: turfrunner@netmailo.com

```html
<!DOCTYPE html>
<html lang="en">
<head>
<meta charset="utf-8">
<title>Gumleaf Plant Hire – Business Card</title>
<link rel="stylesheet" href="https://fonts.googleapis.com/css2?family=Montserrat:wght@700&family=Questrial&display=swap">
<style>
  :root {
    --page: #e9e4df;
    --card-dark: #1d0b0a;
    --card-mid: #4a2220;
    --ink: #3a1a18;
    --ink-soft: #2b1413;
    --light-text: #cfc7c5;
    --rule: #8b7572;
    --white: #ffffff;
    --mark: #5a2f2b;
  }
  * { box-sizing: border-box; margin: 0; padding: 0; }
  html, body { width: 1200px; height: 1000px; overflow: hidden; }
  body {
    background: var(--page);
    font-family: "Questrial", "Helvetica Neue", Arial, sans-serif;
    position: relative;
  }
  .card {
    position: absolute;
    left: 220px;
    width: 760px;
    height: 434px;
    border-radius: 26px;
    overflow: hidden;
    background: radial-gradient(ellipse at 50% 40%, var(--card-mid) 0%, #2c1311 55%, var(--card-dark) 100%);
    box-shadow: 0 6px 18px rgba(0,0,0,0.18);
  }
  .card--front { top: 46px; }
  .card--back { top: 516px; }

  /* Front */
  .brand {
    position: absolute;
    left: 0; right: 0; top: 180px;
    display: flex;
    align-items: center;
    justify-content: center;
    gap: 22px;
  }
  .brand__dot {
    width: 70px; height: 70px;
    border-radius: 50%;
    background: var(--mark);
  }
  .brand__name {
    font-size: 34px;
    color: var(--light-text);
    letter-spacing: 0.5px;
  }

  /* Back */
  .back__panel { position: absolute; inset: 0; }
  .back__mark {
    position: absolute;
    left: 210px; top: 72px;
    width: 86px; height: 86px;
    border-radius: 50%;
    background: var(--mark);
  }
  .back__rule {
    position: absolute;
    left: 322px; top: 48px;
    width: 1px; height: 128px;
    background: var(--rule);
  }
  .services {
    position: absolute;
    left: 342px; top: 42px;
    list-style: none;
    color: var(--light-text);
    font-size: 24px;
    line-height: 33px;
  }
  .contact-name {
    position: absolute;
    left: 0; right: 0; top: 230px;
    text-align: center;
    font-family: "Montserrat", "Helvetica Neue", Arial, sans-serif;
    font-weight: 700;
    font-size: 25px;
    color: var(--ink);
  }
  .address {
    position: absolute;
    left: 40px; top: 282px;
    color: var(--ink-soft);
    font-style: normal;
    font-size: 22px;
    line-height: 32px;
  }
  .address__line { display: flex; align-items: center; gap: 6px; }
  .address__line--indent { padding-left: 24px; }
  .address__po strong {
    font-family: "Montserrat", "Helvetica Neue", Arial, sans-serif;
    font-weight: 700;
    margin-right: 6px;
  }
  .reach {
    position: absolute;
    left: 400px; top: 278px;
    color: var(--ink-soft);
    font-size: 22px;
    line-height: 34px;
    list-style: none;
  }
  .reach li { display: flex; align-items: center; gap: 8px; }
  .reach__icon {
    width: 22px; height: 22px;
    border-radius: 50%;
    background: var(--ink-soft);
    display: inline-flex; align-items: center; justify-content: center;
  }
  .abn {
    position: absolute;
    right: 56px; bottom: 30px;
    font-size: 14px;
    color: var(--ink-soft);
  }
</style>
</head>
<body>

<section class="card card--front" aria-label="Card front">
  <div class="brand">
    <span class="brand__dot" aria-hidden="true"></span>
    <span class="brand__name">Gumleaf Plant Hire Pty Ltd</span>
  </div>
</section>

<section class="card card--back" aria-label="Card back">
  <svg class="back__panel" width="760" height="434" viewBox="0 0 760 434" aria-hidden="true">
    <path d="M0 262 Q 360 168 760 198 L760 434 L0 434 Z" fill="var(--white)"/>
  </svg>

  <span class="back__mark" aria-hidden="true"></span>
  <span class="back__rule" aria-hidden="true"></span>
  <ul class="services">
    <li>Blowers</li>
    <li>Turf Cutter</li>
    <li>Brushcutters</li>
    <li>Lawn mowers with catchers</li>
  </ul>

  <h2 class="contact-name">YOUR NAME HERE</h2>

  <address class="address">
    <div class="address__line">
      <svg width="18" height="24" viewBox="0 0 18 24" aria-hidden="true">
        <path d="M9 0C4 0 0 4 0 9c0 6.5 9 15 9 15s9-8.5 9-15C18 4 14 0 9 0z" fill="var(--ink-soft)"/>
        <circle cx="9" cy="9" r="3.5" fill="var(--white)"/>
      </svg>
      <span>17C Korrin Street</span>
    </div>
    <div class="address__line address__line--indent">Carrowvale Qld 4731</div>
    <div class="address__line address__po"><strong>PO Box</strong>8150 Carrowvale Qld 4731</div>
  </address>

  <ul class="reach">
    <li>
      <span class="reach__icon" aria-hidden="true">
        <svg width="12" height="12" viewBox="0 0 12 12"><path d="M2.5 1l2 2.5-1.2 1.2a6 6 0 0 0 4 4L8.5 7.5 11 9.5 9.8 11C5 11 1 7 1 2.2z" fill="var(--white)"/></svg>
      </span>0417302968
    </li>
    <li>
      <span class="reach__icon" aria-hidden="true">
        <svg width="12" height="12" viewBox="0 0 12 12"><rect x="3" y="1" width="6" height="10" rx="1" fill="var(--white)"/><rect x="4" y="2.5" width="4" height="5" fill="var(--ink-soft)"/></svg>
      </span>0438715024
    </li>
    <li>
      <span class="reach__icon" aria-hidden="true">
        <svg width="12" height="12" viewBox="0 0 12 12"><rect x="1" y="3" width="10" height="7" fill="var(--white)"/><path d="M1 3l5 4 5-4" stroke="var(--ink-soft)" fill="none"/></svg>
      </span>turfrunner@netmailo.com
    </li>
  </ul>

  <p class="abn">ABN: 81 327 905 168</p>
</section>

</body>
</html>
```